KOR Holding

KOR holding is located in the UAE. In the company, there are several departments covering Hospitality management, Facility Management, interior design and Construction.

The logo should not include the name holding, Just KOR.

Needed Items:

(1) Logo.
(2) Business Card.
(3) Letterhead
(4) Envelope
(5) cd cover
(6) email signature
Updates

The previous brief was misplaced with another competition. Current update is the final.

Target Market(s)

Collaboration with international high end firms.

Industry/Entity Type

Business

Requirements
Must have
• COLOR PREFERENCE Maximum 2 colors, preferably mono-color with different shades.
Nice to have
• Elegant, luxurious, and minimalistic.

```html
<!DOCTYPE html>
<html lang="en">
<head>
<meta charset="utf-8">
<title>KOR Holding — Business Card</title>
<link href="https://fonts.googleapis.com/css2?family=Cinzel:wght@400;500&family=Josefin+Sans:wght@300;400&display=swap" rel="stylesheet">
<style>
  :root {
    --backdrop: #37343b;
    --card: #1f1f28;
    --card-edge: #4a4650;
    --champagne: #ead7c4;
    --champagne-soft: #cdb8a6;
    --pattern-tone: rgba(200, 190, 200, 0.10);
  }
  * { margin: 0; padding: 0; box-sizing: border-box; }
  html, body {
    width: 1200px; height: 1200px; overflow: hidden;
    background: var(--backdrop);
  }
  .canvas { position: relative; width: 1200px; height: 1200px; }

  .card {
    position: absolute; left: 163px; width: 720px; height: 411px;
    background: var(--card);
    border: 1px solid var(--card-edge);
    box-shadow: 0 18px 30px rgba(0,0,0,0.35);
    overflow: hidden;
  }
  .card--front { top: 154px; }
  .card--back { top: 614px; }

  .wordmark {
    position: absolute;
    font-family: "Cinzel", serif;
    font-weight: 400;
    color: var(--champagne);
    line-height: 1;
    letter-spacing: 0.02em;
    transform: translate(-50%, -50%);
    white-space: nowrap;
  }
  .card--front .wordmark { left: 177px; top: 206px; font-size: 100px; }
  .card--back .wordmark { left: 360px; top: 212px; font-size: 155px; }

  .divider {
    position: absolute; left: 333px; top: 85px;
    width: 1px; height: 249px;
    background: linear-gradient(to bottom, transparent, var(--champagne) 15%, var(--champagne) 85%, transparent);
  }

  .contact { position: absolute; left: 372px; top: 92px; color: var(--champagne); }
  .contact__name {
    font-family: "Cinzel", serif; font-weight: 500;
    font-size: 24px; letter-spacing: 0.02em; line-height: 1;
  }
  .contact__role {
    font-family: "Josefin Sans", sans-serif; font-weight: 300;
    font-size: 17px; letter-spacing: 0.08em; margin-top: 7px;
    color: var(--champagne-soft);
  }
  .contact__rule { width: 36px; height: 1px; background: var(--champagne); margin-top: 9px; }
  .contact__address {
    font-family: "Josefin Sans", sans-serif; font-weight: 300;
    font-size: 17px; letter-spacing: 0.14em; line-height: 24px;
    margin-top: 22px; text-transform: uppercase;
  }
  .contact__lines { list-style: none; margin-top: 20px; }
  .contact__lines li {
    display: flex; align-items: center; height: 26px;
    font-family: "Josefin Sans", sans-serif; font-weight: 300;
    font-size: 17px; letter-spacing: 0.14em; text-transform: uppercase;
  }
  .contact__icon { width: 14px; height: 14px; margin-right: 19px; fill: var(--champagne); }

  .pattern-field {
    position: absolute; inset: 0;
    background: linear-gradient(100deg, var(--pattern-tone) 0%, rgba(200,190,200,0.05) 45%, transparent 85%);
  }
</style>
</head>
<body>
<main class="canvas">
  <section class="card card--front" aria-label="Business card front">
    <div class="wordmark">KOR</div>
    <div class="divider"></div>
    <div class="contact">
      <p class="contact__name">DANIEL VERANO</p>
      <p class="contact__role">CEO</p>
      <div class="contact__rule"></div>
      <p class="contact__address">42 Marina Crest Road,<br>Ste DU 40217</p>
      <ul class="contact__lines">
        <li>
          <svg class="contact__icon" viewBox="0 0 16 16" aria-hidden="true"><path d="M3.5 1.5l2.6 2.6-1.4 1.9c.9 2 2.3 3.4 4.3 4.3l1.9-1.4 2.6 2.6-1.8 2.3C6.6 13.4 2.6 9.4 1.2 3.3z"/></svg>
          (415) 555.0142
        </li>
        <li>
          <svg class="contact__icon" viewBox="0 0 16 16" aria-hidden="true"><path d="M4 1h8v4H4zM1 6h14v6h-2v-2H3v2H1zM4 11h8v4H4z"/></svg>
          (415) 555.0199
        </li>
        <li>
          <svg class="contact__icon" viewBox="0 0 16 16" aria-hidden="true"><path d="M1 3h14v10H1zM2.2 4.2v.4L8 9l5.8-4.4v-.4zM2.2 6.1v5.7h11.6V6.1L8 10.5z"/></svg>
          www.korhq.com
        </li>
      </ul>
    </div>
  </section>

  <section class="card card--back" aria-label="Business card back">
    <div class="pattern-field" role="img" aria-label="Faint geometric line pattern across the card back"></div>
    <div class="wordmark">KOR</div>
  </section>
</main>
</body>
</html>
```